Label Design for RTD Cocktail Line Tovelin Spirits

Tovelin Spirits is a line of Indian-inspired artisan cocktails that "brings the bartender home" for professional men and women who like the finer things in life but don’t always have the time to treat themselves. No need for a multitude of expensive and hard-to-find ingredients, time consuming recipes, or a mixologist.

Our line of 3 open and serve cocktails blends a range of premium spirits with exotic ingredients so you can conveniently raise a glass for any of life’s celebrations.

Our bottle is the 750ml Claret bottle with Quarnet (screw cap) closure and will be covered entirely in a shrink sleeve (so potentially anything can be designed for any part of the bottle). We want the bottle to pop on the shelf so it should look different than what’s already out there (Velvet Moth, Galdrova, Merlusa ready to drink cocktails). We are looking for a sexy design that's polished/sleek.
Updates

Project Deadline Extended
Reason: Hello designers! Tovelin Spirits is so impressed with what we have received thus far and we would like to give some of the designers a few extra days to make the edits we requested. It's never too late to submit! Thank you all!

Industry/Entity Type

It Professional

Requirements
Must have
• Front of bottle
* “Tovelin Spirits” name and Peacock Logo- but feel free to pull the elements apart and use them on the bottle in different ways
* Open & Serve
* 12% ALC/VOL
* 750 ml
* 3 different labels in a theme for
-Borvelle
-Faluntera
-Pomadrine

Borvelle Ideas- soft brown palate, the ingredients in chai spice (cloves, cardamom pods, nutmeg, black peppercorns, star anise, and cinnamon stick)

Faluntera Ideas -cool and refreshing, pale green shade (not clashing with logo), graphics of fresh mint leaves, green chili, lime, cucumber

Pomadrine Ideas- soft/pale pink shades, graphics of lychi fruit (outer red shell and inner pink flesh), ginger

Back of bottle
* explanation of the 3 cocktails
Borvelle: Forget what you think you know about chai, this is not the Queen’s tea-time drink! Borvelle is a smooth, sweetly -spiced cocktail made with vodka, black tea, and a combination of aromatic spices. This velvety cocktail is rich without being heavy. Enjoy chilled or over ice anytime.

Faluntera: Faluntera can’t make up its mind! This fusion of zesty lime, sweet mint, earthy cucumber and spicy chilies is so refreshing you’ll crave it on a hot summer day or a cool winter’s night. The exotic botanicals in gin add a complexity to the cocktail making this a refreshing but potent drink! Enjoy chilled or over ice anytime.

Pomadrine: East meet West. Delicate lychi meet hard-hitting whiskey. Pomadrine will tempt you senses with flavor, fragrance and beauty. The peppery kick of ginger and the intensity of the un-aged whiskey are softened by lychi’s intoxicating scent and subtle, sweet finish.

Please include
1. Bottled By QRW Spirits Company
2. Sample barcode (where you would place it in your design)
3. www.TovelinSpirits.example
4. GOVERNMENT WARNING: (1) According to the Surgeon General, women should not drink alcoholic beverages during pregnancy because of the risk of birth defects. (2) Consumption of alcoholic beverages impairs your ability to drive a car or operate machinery, and may cause health problems.

Optional to include
*"Bring the Bartender Home"
*"Tovelin Spirits” name and Peacock Logo on the back
*Entirely black sleeve with contrasting design

FYI the Fonts used in our logo are Geosans Light and Prakrta, but feel free to use other complimentary fonts on the other aspects.
Nice to have
• Optional to include

```html
<!DOCTYPE html>
<html lang="en">
<head>
<meta charset="utf-8">
<title>Tovelin Spirits – Open &amp; Serve Cocktail Sleeves</title>
<link rel="stylesheet" href="https://fonts.googleapis.com/css2?family=Pinyon+Script&family=Josefin+Sans:wght@300;400&display=swap">
<style>
  :root{
    --backdrop:#050505;
    --sleeve:#0b0b0c;
    --sleeve-edge:#1c1d20;
    --cap-light:#e2c46c;
    --cap-dark:#8a6a22;
    --brand-teal:#2fa9c6;
    --muted:#8c8c8c;
    --chai:#e6852a;
    --chai-deep:#b4501c;
    --mint:#8fcf6a;
    --mint-deep:#2f9a3a;
    --lychee:#e07fb0;
    --lychee-deep:#b53a7c;
  }
  *{margin:0;padding:0;box-sizing:border-box}
  html,body{width:1200px;height:919px;overflow:hidden;background:var(--backdrop)}
  .canvas{position:relative;width:1200px;height:919px;background:var(--backdrop)}

  .bottle{position:absolute;top:55px;width:200px;height:810px}
  .bottle--chai{left:240px}
  .bottle--mint{left:500px}
  .bottle--lychee{left:760px}
  .bottle__shape{position:absolute;inset:0}

  .brand{position:absolute;top:262px;left:0;width:200px;text-align:center;
    font-family:"Josefin Sans",sans-serif;font-weight:400;color:var(--brand-teal);
    font-size:19px;letter-spacing:1px;line-height:1.05}
  .brand small{display:block;font-size:9px;letter-spacing:3px}

  .flavour{position:absolute;top:382px;left:16px;width:190px;
    font-family:"Pinyon Script",cursive;font-size:38px;line-height:1;white-space:nowrap}
  .bottle--chai .flavour{color:var(--chai)}
  .bottle--mint .flavour{color:var(--mint)}
  .bottle--lychee .flavour{color:var(--lychee)}

  .serve{position:absolute;top:423px;left:100px;
    font-family:"Josefin Sans",sans-serif;font-weight:300;font-size:11px;
    letter-spacing:.5px;color:#d9d9d9;white-space:nowrap}

  .ingredient{position:absolute;top:425px;left:38px;width:48px;height:36px;border-radius:50%}
  .bottle--chai .ingredient{background:radial-gradient(circle at 40% 40%,var(--chai),var(--chai-deep))}
  .bottle--mint .ingredient{background:radial-gradient(circle at 40% 40%,var(--mint),var(--mint-deep))}
  .bottle--lychee .ingredient{background:radial-gradient(circle at 40% 60%,#f3d6e2,var(--lychee-deep))}

  .bloom{position:absolute;top:575px;left:8px;width:184px;height:170px;border-radius:45% 55% 40% 50%;opacity:.85}
  .bottle--chai .bloom{background:radial-gradient(ellipse at 55% 55%,#f36a2a 0%,#e08a26 35%,rgba(180,80,20,.35) 65%,transparent 80%)}
  .bottle--mint .bloom{background:radial-gradient(ellipse at 55% 55%,#9fe08a 0%,#3fbf4a 35%,rgba(40,140,50,.35) 65%,transparent 80%)}
  .bottle--lychee .bloom{background:radial-gradient(ellipse at 55% 55%,#f5a4cf 0%,#e0509a 35%,rgba(170,50,110,.35) 65%,transparent 80%)}

  .abv{position:absolute;top:762px;left:0;width:200px;text-align:center;
    font-family:"Josefin Sans",sans-serif;font-weight:300;font-size:8px;color:var(--muted);line-height:1.3}
</style>
</head>
<body>
<main class="canvas">

  <svg width="0" height="0" style="position:absolute" aria-hidden="true">
    <defs>
      <linearGradient id="cap-foil" x1="0" x2="1">
        <stop offset="0" stop-color="#6e5418"/>
        <stop offset=".35" stop-color="#e8cc78"/>
        <stop offset=".6" stop-color="#c9a243"/>
        <stop offset="1" stop-color="#5e4612"/>
      </linearGradient>
      <linearGradient id="sleeve-sheen" x1="0" x2="1">
        <stop offset="0" stop-color="#151618"/>
        <stop offset=".3" stop-color="#0a0a0b"/>
        <stop offset=".75" stop-color="#0b0b0c"/>
        <stop offset="1" stop-color="#1a1b1e"/>
      </linearGradient>
      <symbol id="claret" viewBox="0 0 200 810">
        <path d="M74 150 L74 175 C74 215 70 235 40 255 C12 275 5 295 5 330 L5 790 Q5 808 22 808 L178 808 Q195 808 195 790 L195 330 C195 295 188 275 160 255 C130 235 126 215 126 175 L126 150 Z" fill="url(#sleeve-sheen)"/>
        <rect x="72" y="3" width="56" height="152" rx="3" fill="url(#cap-foil)"/>
        <rect x="70" y="0" width="60" height="18" rx="3" fill="url(#cap-foil)"/>
      </symbol>
    </defs>
  </svg>

  <article class="bottle bottle--chai">
    <svg class="bottle__shape" viewBox="0 0 200 810" aria-hidden="true"><use href="#claret"/></svg>
    <p class="brand">Tovelin<small>Spirits</small></p>
    <h2 class="flavour">Borvelle</h2>
    <div class="ingredient" role="img" aria-label="Cinnamon sticks illustration"></div>
    <p class="serve">OPEN &amp; SERVE</p>
    <div class="bloom" role="img" aria-label="Layered orange floral bloom artwork"></div>
    <p class="abv">12% ALC/VOL<br>750 ml</p>
  </article>

  <article class="bottle bottle--mint">
    <svg class="bottle__shape" viewBox="0 0 200 810" aria-hidden="true"><use href="#claret"/></svg>
    <p class="brand">Tovelin<small>Spirits</small></p>
    <h2 class="flavour">Faluntera</h2>
    <div class="ingredient" role="img" aria-label="Fresh mint leaves illustration"></div>
    <p class="serve">OPEN &amp; SERVE</p>
    <div class="bloom" role="img" aria-label="Layered green floral bloom artwork"></div>
    <p class="abv">12% ALC/VOL<br>750 ml</p>
  </article>

  <article class="bottle bottle--lychee">
    <svg class="bottle__shape" viewBox="0 0 200 810" aria-hidden="true"><use href="#claret"/></svg>
    <p class="brand">Tovelin<small>Spirits</small></p>
    <h2 class="flavour">Pomadrine</h2>
    <div class="ingredient" role="img" aria-label="Lychee fruit illustration"></div>
    <p class="serve">OPEN &amp; SERVE</p>
    <div class="bloom" role="img" aria-label="Layered pink floral bloom artwork"></div>
    <p class="abv">12% ALC/VOL<br>750 ml</p>
  </article>

</main>
</body>
</html>
```